Design a company PowerPoints presentation

we need to create a PowerPoint presentation that will show the company portfolio and products , with explanation on each product. the products are divided into 3 groups , and then show the main points of each product under each group. with some few slides to describe the company and the field it works with. the main challenge for me is to make the correct layout and relevant pictures for each group or products or for the product itself.

```html
<!DOCTYPE html>
<html lang="en">
<head>
<meta charset="utf-8">
<title>Company Portfolio Presentation – Slide Overview</title>
<link href="https://fonts.googleapis.com/css2?family=Lato:ital,wght@0,400;0,700;0,900;1,400&display=swap" rel="stylesheet">
<style>
:root{
  --orange:#ef5a2a;
  --orange-deep:#e0401b;
  --orange-soft:#f7a35c;
  --ink:#2b2b2b;
  --muted:#8a8a8a;
  --line:#d9d9d9;
  --paper:#f4f4f4;
  --white:#ffffff;
  --dark:#161616;
}
*{box-sizing:border-box;margin:0;padding:0}
html,body{width:1200px;height:576px;overflow:hidden;background:var(--white);font-family:"Lato",sans-serif;color:var(--ink)}
.deck{position:absolute;left:38px;top:34px;display:grid;grid-template-columns:repeat(5,219px);grid-auto-rows:121px;column-gap:7.5px;row-gap:8px}
.slide{position:relative;background:var(--paper);overflow:hidden;box-shadow:0 2px 5px rgba(0,0,0,.12);font-size:3px;line-height:1.35}
.slide svg{display:block}
.accent{position:absolute;left:6px;top:4px;width:6px;height:1px;background:var(--orange)}
.accent::after{content:"";position:absolute;left:7px;top:0;width:1.5px;height:1px;background:var(--orange)}
.title{position:absolute;left:6px;top:8px;font-size:7px;font-weight:700;color:var(--ink);line-height:1.2}
.sub{position:absolute;left:6px;top:18px;font-size:2.4px;color:var(--muted)}
.foot-url{position:absolute;left:6px;bottom:6px;font-size:2.6px;color:var(--muted)}
.foot-url b{color:var(--ink)}
.foot-page{position:absolute;right:6px;bottom:6px;font-size:2.6px;color:var(--ink)}
.foot-page i{display:inline-block;width:.5px;height:4px;background:var(--orange);margin:0 3px;vertical-align:middle}
.bar{position:absolute;left:0;right:0;bottom:0;height:1.5px;background:var(--orange)}
.bar::after{content:"";position:absolute;left:50%;width:15%;top:0;height:1.5px;background:#c9c9c9}
.tiny{font-size:2.3px;color:var(--muted);line-height:1.4}
.ph,.abs{position:absolute}
.center{text-align:center}
/* cover */
.cover .brand{position:absolute;left:0;right:0;top:42px;text-align:center;font-size:5px;font-weight:700;letter-spacing:.2px}
.cover h1{position:absolute;left:0;right:0;top:54px;text-align:center;font-size:7.5px;font-weight:700;line-height:1.2}
.cover .csub{position:absolute;left:0;right:0;top:66px;text-align:center;font-size:3.4px}
.cover .who{position:absolute;left:0;right:0;top:86px;text-align:center;font-size:4px;font-weight:700}
.cover .who span{color:var(--orange)}
.cover .date{position:absolute;left:10px;bottom:7px;font-size:2.6px}
.cover .date span{color:var(--orange)}
.cover .url{position:absolute;right:10px;bottom:7px;font-size:2.6px}
.cover-dark{background:radial-gradient(ellipse at 60% 45%,#3a1a10 0%,var(--dark) 60%);color:var(--white)}
.cover-light{background:var(--white)}
/* list */
.toc{position:absolute;top:38px;width:66px;font-size:2.6px;font-weight:700}
.toc div{display:flex;justify-content:space-between;border-bottom:.5px solid var(--line);padding-bottom:2px;margin-bottom:12.5px}
.toc .on{color:var(--orange);border-color:var(--orange)}
/* mission */
.mission-box{position:absolute;left:23px;top:29px;width:174px;height:69px;background:var(--orange);color:var(--white);font-size:4px;font-style:italic;text-align:center;padding:22px 16px 0;line-height:2.2;box-shadow:0 2px 4px rgba(0,0,0,.2)}
.mission-box::before{content:"";position:absolute;left:82px;top:20px;width:10px;height:.5px;background:var(--white)}
/* focus */
.month{position:absolute;width:54px;text-align:center}
.month b{display:block;font-size:3.2px;font-weight:400;color:var(--ink);margin-bottom:2px}
.month b::after{content:"";display:block;width:4px;height:.5px;background:var(--orange);margin:1.5px auto 0}
.month.lift{background:var(--white);box-shadow:0 1px 3px rgba(0,0,0,.12);padding:6px 2px 8px;top:26px}
/* stats */
.stat{position:absolute;top:72px;width:50px;text-align:center}
.stat b{display:block;font-size:6px;font-weight:400;line-height:1.2}
.stat span{font-size:2.4px;color:var(--muted)}
/* money */
.money{position:absolute;left:152px;width:48px;height:24px;border:.6px solid #cfcfcf;background:var(--white)}
.money span{position:absolute;left:4px;top:3px;font-size:2.6px;color:var(--muted)}
.money b{position:absolute;right:3px;bottom:3px;font-size:7px;font-weight:400;line-height:1}
.money.hot{border-color:var(--orange)}
.money.hot span,.money.hot b{color:var(--orange)}
/* calendar */
.cal{position:absolute;top:39px;width:50px;height:58px;background:var(--white);box-shadow:0 1px 3px rgba(0,0,0,.15);text-align:center;padding-top:6px}
.cal svg{margin:0 auto}
.cal b{display:block;font-size:4px;color:var(--orange);font-weight:400;margin-top:2px;line-height:1.1}
.cal ul{text-align:left;margin:4px 0 0 5px;font-size:2.1px;color:var(--muted);list-style:none;line-height:1.9}
.cal li::before{content:"• ";color:var(--orange)}
/* marketing */
.process{background:linear-gradient(135deg,#5b6068,#3c4047)}
.process .title,.process .foot-url,.process .foot-page,.process .foot-url b{color:var(--white)}
.pcard{position:absolute;top:44px;width:42px;height:56px;border:.6px solid var(--orange);border-top:none;border-radius:0 0 4px 4px;background:rgba(0,0,0,.12);color:var(--white);font-size:2.2px;padding:22px 5px 0;line-height:1.5}
.pcard b{display:block;font-size:2.6px;margin-bottom:3px}
.pnum{position:absolute;top:32px;width:20px;height:20px;border-radius:50%;background:var(--orange-deep);box-shadow:0 0 0 2px rgba(255,255,255,.15);color:var(--white);text-align:center;font-size:5px;padding-top:5.5px;line-height:1}
.pnum small{display:block;font-size:1.8px;margin-top:1px}
/* thanks */
.thanks{background:linear-gradient(135deg,var(--orange) 0%,var(--orange-deep) 100%);color:var(--white)}
.thanks h2{position:absolute;left:0;right:0;top:40px;text-align:center;font-size:14px;font-weight:700;line-height:1.1}
.thanks .rule{position:absolute;left:63px;width:93px;top:58px;height:.5px;background:var(--white)}
.thanks p{position:absolute;left:60px;width:99px;top:62px;font-size:2.2px;text-align:center}
.social{position:absolute;top:80px;width:6px;height:6px;border:.5px solid var(--white);border-radius:50%}
.thanks .foot-url,.thanks .foot-page,.thanks .foot-url b{color:var(--white)}
.icons{background:var(--white)}
</style>
</head>
<body>
<main class="deck">

  <section class="slide cover cover-dark">
    <div class="brand">LUMEN</div>
    <h1>Presentation Tittle Goes Here</h1>
    <div class="csub">Credential Subtittle Presentation</div>
    <div class="who">Mr. Adam <span>Reyes</span></div>
    <div class="date">November <span>2022</span></div>
    <div class="url">www.northwind.co</div>
  </section>

  <section class="slide cover cover-light">
    <div class="brand">LUMEN</div>
    <h1>Presentation Tittle Goes Here</h1>
    <div class="csub" style="color:var(--muted)">Credential Subtittle Presentation</div>
    <div class="who" style="font-weight:400">Mr. Adam <span>Reyes</span></div>
    <div class="date" style="color:var(--muted)">November <span>2022</span></div>
    <div class="url" style="color:var(--muted)">www.northwind.co</div>
  </section>

  <section class="slide">
    <span class="accent"></span><h2 class="title">Presentation List</h2><div class="sub">Here Our Credential Subtitle</div>
    <div class="toc" style="left:29px">
      <div><span>COVER SLIDES</span><span>01</span></div>
      <div class="on"><span>PRESENTATION LIST</span><span>03</span></div>
      <div><span>ABOUT US</span><span>04</span></div>
      <div><span>OUR MISSIONS &amp; VISION</span><span>06</span></div>
    </div>
    <div class="toc" style="left:124px">
      <div><span>INFOGRAPH ONE</span><span>07</span></div>
      <div><span>INFOGRAPH TWO</span><span>08</span></div>
      <div><span>INFOGRAPH THREE</span><span>09</span></div>
      <div><span>CLOSING SLIDES</span><span>10</span></div>
    </div>
    <div class="foot-url">www.<b>northwind</b>.co</div><div class="foot-page">page<i></i>3</div><span class="bar"></span>
  </section>

  <section class="slide">
    <span class="accent"></span><h2 class="title">Our Mission and Vision</h2>
    <div class="mission-box">To utilize cutting-edge technological advances for the advancement of customer-facing services provided by banks, fintech's and acquirers.</div>
    <div class="foot-url">www.<b>northwind</b>.co</div><div class="foot-page">page<i></i>4</div><span class="bar"></span>
  </section>

  <section class="slide">
    <span class="accent"></span><h2 class="title">Our Focuss</h2>
    <div class="month" style="left:12px;top:32px"><b>June</b><p class="tiny">Launch of Group A payment gateway for partner banks.</p></div>
    <div class="month lift" style="left:82px"><b>July</b><p class="tiny">Group A card issuing module goes live for clients.</p></div>
    <div class="month" style="left:152px;top:32px"><b>August</b><p class="tiny">Group B mobile banking app opens to first users.</p></div>
    <div class="month" style="left:12px;top:75px"><b>September</b><p class="tiny">Group B onboarding portal rolled out to branches.</p></div>
    <div class="month" style="left:82px;top:75px"><b>October</b><p class="tiny">Group C fraud analytics suite enters full release.</p></div>
    <div class="month" style="left:152px;top:75px"><b>November</b><p class="tiny">Group C reporting dashboard shared with acquirers.</p></div>
    <div class="foot-url">www.<b>northwind</b>.co</div><div class="foot-page">page<i></i>5</div><span class="bar"></span>
  </section>

  <section class="slide">
    <span class="accent"></span><h2 class="title">About Our Company</h2>
    <div class="ph" role="img" aria-label="Photo of hands typing on a laptop" style="left:21px;top:29px;width:64px;height:54px;background:linear-gradient(135deg,#8c9aa6,#4b5661);box-shadow:0 1px 3px rgba(0,0,0,.2)"></div>
    <div class="abs tiny" style="left:101px;top:37px;width:100px">
      <p>We build digital products for banks, fintechs and acquirers, shaped around clear service, steady growth and trust in every line we offer.</p>
      <p style="margin-top:3px">Our portfolio spans three product groups.</p>
      <p style="margin-top:3px">Payments, Digital Banking and Data &amp; Risk each answer one real client need and scale with them.</p>
    </div>
    <div class="foot-url">www.<b>northwind</b>.co</div><div class="foot-page">page<i></i>6</div><span class="bar"></span>
  </section>

  <section class="slide">
    <span class="accent"></span><h2 class="title">The Awards</h2>
    <div class="ph" role="img" aria-label="Laptop lit in pink light" style="left:15px;top:26px;width:50px;height:31px;background:linear-gradient(135deg,#1b1030,#c02a6a)"></div>
    <div class="ph" role="img" aria-label="Person working on a laptop at a desk" style="left:84px;top:26px;width:50px;height:31px;background:linear-gradient(135deg,#cfcfcf,#6c6c6c)"></div>
    <div class="ph" role="img" aria-label="Dark keyboard with teal glow" style="left:153px;top:26px;width:50px;height:31px;background:linear-gradient(135deg,#0d2d33,#1b8c8c)"></div>
    <div class="abs center" style="left:15px;top:66px;width:50px;font-size:3px">2020<p class="tiny" style="margin-top:5px">Best payments product for our gateway suite.</p></div>
    <div class="abs center" style="left:84px;top:66px;width:50px;font-size:3px">2021<p class="tiny" style="margin-top:5px">Top digital banking app of the regional year.</p></div>
    <div class="abs center" style="left:153px;top:65px;width:50px;font-size:3px">2022<p class="tiny" style="margin-top:5px">Risk and data award for our fraud analytics.</p></div>
    <div class="foot-url">www.<b>northwind</b>.co</div><div class="foot-page">page<i></i>7</div><span class="bar"></span>
  </section>

  <section class="slide">
    <span class="accent"></span><h2 class="title">Picture Page with Tittle</h2>
    <div class="ph" role="img" aria-label="Desktop screen showing a product website" style="left:15px;top:31px;width:45px;height:52px;background:linear-gradient(135deg,#e9eef5,#8fa3c4)"></div>
    <div class="ph" role="img" aria-label="Laptop with code on screen" style="left:63px;top:52px;width:44px;height:52px;background:linear-gradient(135deg,#f2f2f2,#3a3f46);box-shadow:0 1px 3px rgba(0,0,0,.2)"></div>
    <div class="abs" style="left:114px;top:36px;width:92px;font-size:4px;color:var(--muted);line-height:1.5"><span style="color:var(--orange)">Group A</span> Payments: gateway, card issuing and merchant tools</div>
    <div class="abs tiny" style="left:114px;top:53px;width:92px"><p><b style="color:var(--ink)">Payment Gateway</b> routes card and wallet payments in real time, with smart retries, clear fees and full reports for every merchant.</p><p style="margin-top:3px"><b style="color:var(--ink)">Card Issuing</b> lets banks launch virtual and physical cards in days, with limits and controls.</p></div>
    <div class="foot-url">www.<b>northwind</b>.co</div><div class="foot-page">page<i></i>8</div><span class="bar"></span>
  </section>

  <section class="slide">
    <span class="accent"></span><h2 class="title">Content Page with Tittle</h2><div class="sub">Here Our Credential Subtitle</div>
    <div class="abs" style="left:105px;top:37px;width:8px;height:.5px;background:var(--orange)"></div>
    <p class="abs tiny center" style="left:25px;top:41px;width:170px"><span style="color:var(--orange)">Group B</span> Digital Banking brings the mobile app, the onboarding portal and the open banking API into one platform, so banks serve clients end to end.</p>
    <div class="stat" style="left:14px"><b>320</b><span>Customers Served</span></div>
    <div class="stat" style="left:61px"><b>1281</b><span>Projects Completed</span></div>
    <div class="stat" style="left:108px"><b>8700</b><span>Project Hours</span></div>
    <div class="stat" style="left:155px"><b>14</b><span>Certifications</span></div>
    <div class="foot-url">www.<b>northwind</b>.co</div><div class="foot-page">page<i></i>9</div><span class="bar"></span>
  </section>

  <section class="slide">
    <span class="accent"></span><h2 class="title">Presentation Content</h2>
    <svg class="abs" style="left:0;top:0" width="219" height="121" viewBox="0 0 219 121" aria-hidden="true">
      <line x1="8" y1="62" x2="208" y2="62" stroke="#c9c9c9" stroke-width=".4"/>
      <g fill="var(--orange-soft)" stroke="#fbd9bf" stroke-width="1.5">
        <circle cx="29" cy="62" r="4"/><circle cx="56" cy="62" r="4"/><circle cx="83" cy="62" r="4"/><circle cx="110" cy="62" r="4"/><circle cx="164" cy="62" r="4"/>
      </g>
      <circle cx="137" cy="62" r="5" fill="var(--orange)" stroke="#fbc9b3" stroke-width="2"/>
      <g fill="#fff" font-size="2.2" text-anchor="middle" font-family="Lato,sans-serif">
        <text x="29" y="63">2018</text><text x="56" y="63">2019</text><text x="83" y="63">2020</text><text x="110" y="63">2021</text><text x="137" y="63">2022</text><text x="164" y="63">2023</text>
      </g>
      <g stroke="var(--orange)" stroke-width=".4" stroke-dasharray="1 1">
        <line x1="56" y1="48" x2="56" y2="57"/><line x1="110" y1="48" x2="110" y2="57"/><line x1="164" y1="48" x2="164" y2="57"/>
        <line x1="29" y1="67" x2="29" y2="75"/><line x1="83" y1="67" x2="83" y2="75"/><line x1="137" y1="68" x2="137" y2="78"/>
      </g>
      <g fill="none" stroke="#333" stroke-width=".5">
        <rect x="53" y="28" width="5" height="4"/><circle cx="110" cy="30" r="2"/><rect x="162" y="28" width="5" height="4"/>
        <circle cx="29" cy="78" r="1.5"/><path d="M82 78 l1 -3 l1 3z"/>
      </g>
    </svg>
    <div class="abs center tiny" style="left:36px;top:35px;width:40px"><b style="color:var(--ink)">Gateway</b><br>Payments group starts.</div>
    <div class="abs center tiny" style="left:90px;top:35px;width:40px"><b style="color:var(--ink)">Mobile App</b><br>Banking group starts.</div>
    <div class="abs center tiny" style="left:144px;top:35px;width:40px"><b style="color:var(--ink)">Risk Suite</b><br>Data group goes live.</div>
    <div class="abs center tiny" style="left:9px;top:82px;width:40px"><b style="color:var(--ink)">Founded</b><br>First bank client signed.</div>
    <div class="abs center tiny" style="left:63px;top:82px;width:40px"><b style="color:var(--ink)">Card Issuing</b><br>New payments product.</div>
    <div class="abs center tiny" style="left:117px;top:82px;width:40px"><b style="color:var(--orange)">The Goal</b><br>All three groups live.</div>
    <div class="foot-url">www.<b>northwind</b>.co</div><div class="foot-page">page<i></i>10</div><span class="bar"></span>
  </section>

  <section class="slide">
    <span class="accent"></span><h2 class="title">Profit Report with Chart</h2>
    <div class="abs tiny" style="left:19px;top:37px;width:56px"><p>Profit grew each quarter as new clients joined the Digital Banking group this year.</p><p style="margin-top:3px">Payments costs stayed flat.</p><p style="margin-top:3px">Data &amp; Risk margins rose in the last two months of the half.</p></div>
    <svg class="abs" style="left:88px;top:38px" width="50" height="50" viewBox="0 0 50 50" aria-label="Donut chart of monthly profit">
      <g fill="none" stroke-width="5">
        <circle cx="25" cy="25" r="20" stroke="var(--orange-soft)" stroke-dasharray="25 126"/>
        <circle cx="25" cy="25" r="20" stroke="var(--orange)" stroke-dasharray="22 126" stroke-dashoffset="-25"/>
        <circle cx="25" cy="25" r="20" stroke="#f58a3c" stroke-dasharray="21 126" stroke-dashoffset="-47"/>
        <circle cx="25" cy="25" r="20" stroke="var(--orange-deep)" stroke-dasharray="20 126" stroke-dashoffset="-68"/>
        <circle cx="25" cy="25" r="20" stroke="#fbc08a" stroke-dasharray="20 126" stroke-dashoffset="-88"/>
        <circle cx="25" cy="25" r="20" stroke="#f26d32" stroke-dasharray="18 126" stroke-dashoffset="-108"/>
      </g>
    </svg>
    <div class="abs tiny" style="left:87px;top:90px">■ Jan ■ Feb ■ Marc ■ Apr ■ May ■ Jun</div>
    <div class="money" style="top:33px"><span>June</span><b>$2700</b></div>
    <div class="money hot" style="top:63px"><span>March</span><b>$3600</b></div>
    <div class="foot-url">www.<b>northwind</b>.co</div><div class="foot-page">page<i></i>11</div><span class="bar"></span>
  </section>

  <section class="slide">
    <span class="accent"></span><h2 class="title">Step with Infograph</h2><div class="sub">Here Our Credential Subtitle</div>
    <svg class="abs" style="left:0;top:38px" width="219" height="40" viewBox="0 0 219 40" aria-hidden="true">
      <g fill="#fff" stroke="#fbd5c4" stroke-width=".6">
        <path d="M29 2 l13 7 v14 l-13 7 l-13 -7 v-14z"/><path d="M69 2 l13 7 v14 l-13 7 l-13 -7 v-14z"/><path d="M109 2 l13 7 v14 l-13 7 l-13 -7 v-14z"/><path d="M149 2 l13 7 v14 l-13 7 l-13 -7 v-14z"/><path d="M188 2 l13 7 v14 l-13 7 l-13 -7 v-14z"/>
      </g>
      <g stroke="#bbb" stroke-width=".4" stroke-dasharray="1 1"><line x1="45" y1="16" x2="53" y2="16"/><line x1="85" y1="16" x2="93" y2="16"/><line x1="125" y1="16" x2="133" y2="16"/><line x1="165" y1="16" x2="172" y2="16"/></g>
      <g fill="var(--orange)" font-size="2.4" text-anchor="middle" font-family="Lato,sans-serif"><text x="29" y="17">Step 1</text><text x="69" y="17">Step 2</text><text x="109" y="17">Step 3</text><text x="149" y="17">Step 4</text><text x="188" y="17">Step 5</text></g>
    </svg>
    <div class="abs center tiny" style="left:12px;top:80px;width:34px"><b style="color:var(--ink)">Marketing Step</b><br>Find bank needs.</div>
    <div class="abs center tiny" style="left:52px;top:80px;width:34px"><b style="color:var(--ink)">Production Step</b><br>Build the product.</div>
    <div class="abs center tiny" style="left:92px;top:80px;width:34px"><b style="color:var(--ink)">R&amp;D Step</b><br>Test with pilots.</div>
    <div class="abs center tiny" style="left:132px;top:80px;width:34px"><b style="color:var(--ink)">Vendor Step</b><br>Certify partners.</div>
    <div class="abs center tiny" style="left:171px;top:80px;width:34px"><b style="color:var(--ink)">Supplier Step</b><br>Host and support.</div>
    <div class="foot-url">www.<b>northwind</b>.co</div><div class="foot-page">page<i></i>12</div><span class="bar"></span>
  </section>

  <section class="slide">
    <span class="accent"></span><h2 class="title">The Next Step for Closer</h2>
    <svg class="abs" style="left:0;top:0" width="219" height="121" viewBox="0 0 219 121" aria-hidden="true">
      <defs><linearGradient id="pill" x1="0" y1="0" x2="0" y2="1"><stop offset="0" stop-color="#4a4f57"/><stop offset=".55" stop-color="#4a4f57"/><stop offset=".56" stop-color="#ef5a2a"/><stop offset="1" stop-color="#e0401b"/></linearGradient></defs>
      <g fill="url(#pill)"><rect x="22" y="33" width="16" height="33" rx="8"/><rect x="70" y="33" width="16" height="33" rx="8"/><rect x="118" y="33" width="16" height="33" rx="8"/><rect x="166" y="33" width="16" height="33" rx="8"/></g>
      <g fill="#fff" font-size="2.6" text-anchor="middle" font-family="Lato,sans-serif"><text x="30" y="50">One</text><text x="78" y="50">Two</text><text x="126" y="50">Three</text><text x="174" y="50">Four</text></g>
      <g fill="var(--orange)" stroke="#fbd0bd" stroke-width="1.2"><circle cx="30" cy="91" r="5"/><circle cx="78" cy="91" r="5"/><circle cx="126" cy="91" r="5"/><circle cx="174" cy="91" r="5"/></g>
      <g fill="none" stroke="#fff" stroke-width=".5"><circle cx="30" cy="91" r="2"/><path d="M78 89 v4 M76 91 h4"/><rect x="124.5" y="89.5" width="3" height="3"/><path d="M172 93 l2 -3 l2 2"/></g>
    </svg>
    <div class="abs center tiny" style="left:9px;top:70px;width:42px">Demo the product group that fits the client.</div>
    <div class="abs center tiny" style="left:57px;top:70px;width:42px">Agree scope, pricing and rollout plan.</div>
    <div class="abs center tiny" style="left:105px;top:70px;width:42px">Run a short pilot with live users.</div>
    <div class="abs center tiny" style="left:153px;top:70px;width:42px">Sign and launch with full support.</div>
    <div class="foot-url">www.<b>northwind</b>.co</div><div class="foot-page">page<i></i>13</div><span class="bar"></span>
  </section>

  <section class="slide process">
    <span class="accent"></span><h2 class="title">Step Marketing Process</h2>
    <div class="pcard" style="left:17px"><b>Step One</b>Target banks for the Payments group.</div>
    <div class="pcard" style="left:65px"><b>Step Two</b>Pitch Digital Banking to fintech leads.</div>
    <div class="pcard" style="left:113px"><b>Step Three</b>Offer Data &amp; Risk to acquirers.</div>
    <div class="pcard" style="left:161px"><b>Step Four</b>Bundle all three groups for growth.</div>
    <div class="pnum" style="left:28px">450<small>Point A</small></div>
    <div class="pnum" style="left:76px">460<small>Point B</small></div>
    <div class="pnum" style="left:124px">480<small>Point C</small></div>
    <div class="pnum" style="left:172px">490<small>Point D</small></div>
    <div class="foot-url">www.<b>northwind</b>.co</div><div class="foot-page">page<i></i>14</div><span class="bar"></span>
  </section>

  <section class="slide">
    <span class="accent"></span><h2 class="title">Montly Calendar Planning</h2>
    <div class="cal" style="left:25px"><svg width="6" height="6" viewBox="0 0 6 6" aria-hidden="true"><circle cx="3" cy="3" r="2.5" fill="var(--orange)"/></svg><b>23<sup style="font-size:2px">rd</sup></b><span class="tiny">June</span><ul><li>Gateway release</li><li>Bank demo day</li><li>Merchant training</li><li>Launch report</li></ul></div>
    <div class="cal" style="left:85px"><svg width="6" height="6" viewBox="0 0 6 6" aria-hidden="true"><circle cx="3" cy="3" r="1" fill="var(--orange)"/><circle cx="1" cy="1" r=".7" fill="var(--orange)"/><circle cx="5" cy="1" r=".7" fill="var(--orange)"/><circle cx="1" cy="5" r=".7" fill="var(--orange)"/><circle cx="5" cy="5" r=".7" fill="var(--orange)"/></svg><b>11<sup style="font-size:2px">st</sup></b><span class="tiny">July</span><ul><li>App beta opens</li><li>User feedback</li><li>Portal update</li><li>Partner review</li></ul></div>
    <div class="cal" style="left:145px"><svg width="6" height="6" viewBox="0 0 6 6" aria-hidden="true"><rect x=".5" y="1" width="5" height="4" fill="none" stroke="var(--orange)" stroke-width=".6"/></svg><b>2<sup style="font-size:2px">nd</sup></b><span class="tiny">August</span><ul><li>Risk suite pilot</li><li>Data workshop</li><li>Model tuning</li><li>Client sign-off</li></ul></div>
    <div class="foot-url">www.<b>northwind</b>.co</div><div class="foot-page">page<i></i>15</div><span class="bar"></span>
  </section>

  <section class="slide">
    <span class="accent"></span><h2 class="title">Monthly Report Chart</h2>
    <svg class="abs" style="left:0;top:0" width="219" height="121" viewBox="0 0 219 121" aria-label="Line chart of monthly figures">
      <polyline points="27,57 47,47 67,66 87,58 107,64 127,59" fill="none" stroke="var(--orange)" stroke-width=".8"/>
      <g font-size="2.4" fill="#444" font-family="Lato,sans-serif" text-anchor="middle">
        <text x="27" y="56">60</text><text x="47" y="46">78</text><text x="67" y="69">49</text><text x="87" y="57">60</text><text x="107" y="67">49</text><text x="130" y="58">56</text>
        <g fill="#999" font-size="2"><text x="25" y="96">JAN</text><text x="45" y="96">FEB</text><text x="66" y="96">MARC</text><text x="86" y="96">APR</text><text x="107" y="96">MAY</text><text x="127" y="96">JUN</text></g>
      </g>
      <path d="M153 33 l4 2.3 v4.6 l-4 2.3 l-4 -2.3 v-4.6z" fill="var(--orange)"/>
      <path d="M153 69 l4 2.3 v4.6 l-4 2.3 l-4 -2.3 v-4.6z" fill="var(--orange)"/>
      <g fill="#fff" font-size="2.6" text-anchor="middle" font-family="Lato,sans-serif"><text x="153" y="38.5">49</text><text x="153" y="74.5">56</text></g>
    </svg>
    <div class="abs" style="left:149px;top:44px;font-size:5px">May</div>
    <p class="abs tiny" style="left:149px;top:53px;width:60px">Payments volume dipped as banks moved to the new gateway.</p>
    <div class="abs" style="left:149px;top:80px;font-size:5px">Jun</div>
    <p class="abs tiny" style="left:149px;top:89px;width:60px">Volume rose again with the app and risk suite in use.</p>
    <div class="foot-url">www.<b>northwind</b>.co</div><div class="foot-page">page<i></i>16</div><span class="bar"></span>
  </section>

  <section class="slide">
    <span class="accent"></span><h2 class="title">Three Poin Strategy</h2>
    <svg class="abs" style="left:0;top:0" width="219" height="121" viewBox="0 0 219 121" aria-label="Three connected strategy points">
      <g stroke="var(--orange)" stroke-width="4" stroke-linecap="round"><line x1="33" y1="59" x2="62" y2="80"/><line x1="62" y1="80" x2="92" y2="45"/></g>
      <g fill="var(--orange-deep)" stroke="#fff" stroke-width="1.5"><circle cx="33" cy="59" r="9"/><circle cx="62" cy="80" r="9"/><circle cx="92" cy="45" r="9"/></g>
      <g fill="#fff" font-family="Lato,sans-serif" text-anchor="middle"><text x="33" y="60" font-size="5">1</text><text x="62" y="81" font-size="5">2</text><text x="92" y="46" font-size="5">3</text><g font-size="1.8"><text x="33" y="64">56%</text><text x="62" y="85">76%</text><text x="92" y="50">89%</text></g></g>
    </svg>
    <div class="abs" style="left:127px;top:33px;width:82px"><span style="font-size:5px">56%</span><p class="tiny">Group A Payments: grow merchant reach and card issuing.</p></div>
    <div class="abs" style="left:127px;top:53px;width:82px"><span style="font-size:5px">76%</span><p class="tiny">Group B Digital Banking: scale the app and open API.</p></div>
    <div class="abs" style="left:127px;top:73px;width:82px"><span style="font-size:5px">89%</span><p class="tiny">Group C Data &amp; Risk: cut fraud and sharpen reports.</p></div>
    <div class="foot-url">www.<b>northwind</b>.co</div><div class="foot-page">page<i></i>17</div><span class="bar"></span>
  </section>

  <section class="slide">
    <span class="accent"></span><h2 class="title">Timeline Chart</h2>
    <svg class="abs" style="left:0;top:0" width="219" height="121" viewBox="0 0 219 121" aria-hidden="true">
      <line x1="16" y1="83" x2="203" y2="83" stroke="#bbb" stroke-width=".4" stroke-dasharray="1 1"/>
      <g stroke="var(--orange)" stroke-width=".6"><line x1="46" y1="47" x2="46" y2="83"/><line x1="77" y1="32" x2="77" y2="83"/><line x1="109" y1="47" x2="109" y2="83"/><line x1="140" y1="32" x2="140" y2="83"/><line x1="171" y1="47" x2="171" y2="83"/></g>
      <g fill="var(--orange-soft)" stroke="#fde1cb" stroke-width="1.5"><circle cx="46" cy="47" r="8"/><circle cx="109" cy="47" r="8"/><circle cx="171" cy="47" r="8"/></g>
      <g fill="var(--orange-deep)" stroke="#fbcdbb" stroke-width="1.5"><circle cx="77" cy="32" r="8"/><circle cx="140" cy="32" r="8"/></g>
      <g fill="var(--orange)" stroke="#fff" stroke-width=".6"><circle cx="46" cy="83" r="1.8"/><circle cx="77" cy="83" r="1.8"/><circle cx="109" cy="83" r="1.8"/><circle cx="140" cy="83" r="1.8"/><circle cx="171" cy="83" r="1.8"/></g>
      <g fill="#fff" font-size="3.2" text-anchor="middle" font-family="Lato,sans-serif"><text x="46" y="48">2020</text><text x="77" y="33">2021</text><text x="109" y="48">2022</text><text x="140" y="33">2023</text><text x="171" y="48">2024</text></g>
    </svg>
    <div class="abs center tiny" style="left:31px;top:89px;width:30px">Gateway first release.</div>
    <div class="abs center tiny" style="left:62px;top:89px;width:30px">Card issuing added.</div>
    <div class="abs center tiny" style="left:94px;top:89px;width:30px">Mobile app launched.</div>
    <div class="abs center tiny" style="left:125px;top:89px;width:30px">Risk suite released.</div>
    <div class="abs center tiny" style="left:156px;top:89px;width:30px">All groups bundled.</div>
    <div class="foot-url">www.<b>northwind</b>.co</div><div class="foot-page">page<i></i>18</div><span class="bar"></span>
  </section>

  <section class="slide thanks">
    <h2>Thank You</h2>
    <span class="rule"></span>
    <p>Thank you for your time. We look forward to the next steps with each of our three product groups.</p>
    <span class="social" style="left:88px"></span><span class="social" style="left:106px"></span><span class="social" style="left:124px"></span>
    <div class="foot-url">www.<b>northwind</b>.co</div><div class="foot-page">page<i></i>19</div>
  </section>

  <section class="slide icons">
    <svg class="abs" style="left:0;top:0" width="219" height="121" viewBox="0 0 219 121" aria-label="Set of simple orange icons">
      <g fill="none" stroke="var(--orange)" stroke-width=".6">
        <rect x="18" y="29" width="7" height="8"/><circle cx="54" cy="32" r="3"/><path d="M49 37 h10"/><rect x="88" y="28" width="6" height="9"/><circle cx="120" cy="30" r="1.2"/><circle cx="126" cy="36" r="1.2"/><path d="M121 30 h4 v5"/><path d="M156 37 l4 -8 l4 8z"/><path d="M189 37 v-7 M192 37 v-5 M195 37 v-8"/>
        <circle cx="21" cy="58" r="3"/><circle cx="54" cy="57" r="1.5"/><rect x="87" y="54" width="8" height="6"/><circle cx="124" cy="57" r="3.5"/><path d="M124 57 v-3.5 M124 57 l3 2"/><path d="M154 60 l3 -3 l2 2 l4 -4"/><circle cx="191" cy="56" r="3"/><path d="M193 58 l3 3"/>
        <circle cx="21" cy="85" r="3.5"/><path d="M54 80 l2 5 v4 h-4 v-4z"/><circle cx="91" cy="85" r="3.5"/><path d="M121 89 v-3 M124 89 v-5 M127 89 v-4"/><path d="M157 86 a3.5 3.5 0 1 0 3.5 -3.5 v3.5z"/><path d="M188 82 l6 6 M194 82 l-6 6"/>
      </g>
    </svg>
  </section>

</main>
</body>
</html>
```